Voltmark Advisory Grupe Stationary
business cards, letter head, envelopes, fax sheet and shipping label
Voltmark Advisory Grupe Stationary - Energy
Creative Brief
Professional
Tom Wellsby
Operations Manager
Voltmark Advisory Group C/o Miles R. Dunstan Esq., Coral Court and West Ridge Road P.O. Box K-57819
office - 242-555-0193
twellsby@voltmarkadvisorygroup.example
www.voltmarkadvisorygroup.example
USA Cel # 832-555-0146

```html
<!DOCTYPE html>
<html lang="en">
<head>
<meta charset="utf-8">
<title>Voltmark Advisory Group Stationery</title>
<link rel="stylesheet" href="https://fonts.googleapis.com/css2?family=Open+Sans:wght@400;600;700&display=swap">
<style>
  :root {
    --bg: #e9e9e7;
    --paper: #ffffff;
    --blue: #1f7fc3;
    --blue-dark: #155f99;
    --yellow: #f3c31b;
    --ink: #333333;
    --muted: #666666;
    --line: #d9d9d9;
  }
  * { box-sizing: border-box; margin: 0; padding: 0; }
  html, body { width: 1200px; height: 684px; overflow: hidden; }
  body { background: var(--bg); font-family: "Open Sans", Arial, sans-serif; color: var(--ink); position: relative; }
  .sheet { position: absolute; background: var(--paper); box-shadow: 0 2px 8px rgba(0,0,0,.18); overflow: hidden; }
  .swoosh { position: absolute; left: 0; bottom: 0; width: 100%; display: block; }
  .brand { display: flex; align-items: center; gap: 6px; position: absolute; }
  .brand-mark { width: 14px; height: 14px; background: var(--yellow); flex: none; }
  .brand-name { color: var(--blue); font-weight: 700; font-size: 12px; line-height: 1.05; letter-spacing: .2px; text-transform: uppercase; }
  .web { position: absolute; font-size: 9px; color: var(--ink); }

  /* business cards */
  .card-back { left: 29px; top: 235px; width: 225px; height: 190px; border-radius: 8px; }
  .card-back .brand { left: 16px; top: 16px; }
  .card-back .brand-name { font-size: 11px; }
  .card-back .company-details { position: absolute; left: 16px; top: 52px; font-size: 5.4px; line-height: 1.5; color: var(--ink); width: 110px; }
  .card-back .person { position: absolute; left: 128px; top: 60px; border-left: 1px solid var(--line); padding-left: 8px; }
  .card-back .person-name { color: var(--blue); font-weight: 700; font-size: 10px; }
  .card-back .person-title { font-size: 7px; color: var(--ink); }
  .card-front { left: 29px; top: 439px; width: 225px; height: 190px; border-radius: 8px; }
  .card-front .brand { left: 16px; top: 28px; }
  .card-front .brand-name { font-size: 14px; }
  .card-front .brand-mark { width: 18px; height: 18px; }

  /* envelopes */
  .envelope-back { left: 271px; top: 132px; width: 439px; height: 233px; }
  .envelope-back .flap { position: absolute; inset: 0; width: 100%; height: 100%; }
  .envelope-back .brand { left: 50%; top: 20px; transform: translateX(-50%); }
  .envelope-back .brand-name { font-size: 10px; }
  .envelope-back .web { left: 50%; transform: translateX(-50%); bottom: 44px; }
  .envelope-front { left: 271px; top: 389px; width: 439px; height: 240px; }
  .envelope-front .brand { left: 22px; top: 22px; }
  .envelope-front .brand-name { font-size: 12px; }
  .envelope-front .return-address { position: absolute; left: 26px; top: 78px; font-size: 7.5px; line-height: 1.5; }
  .envelope-front .web { right: 24px; bottom: 12px; color: #fff; font-size: 8px; }

  /* letterhead */
  .letterhead { left: 732px; top: 84px; width: 437px; height: 564px; }
  .letterhead .brand { left: 30px; top: 28px; }
  .letterhead .brand-mark { width: 18px; height: 18px; }
  .letterhead .brand-name { font-size: 14px; }
  .letterhead .contact { position: absolute; left: 34px; top: 72px; font-size: 7.5px; line-height: 1.55; }
  .letterhead .web { right: 28px; bottom: 14px; color: #fff; font-size: 8px; }
</style>
</head>
<body>

<svg width="0" height="0" style="position:absolute">
  <defs>
    <symbol id="wave" viewBox="0 0 400 80" preserveAspectRatio="none">
      <path d="M0 40 C120 10 260 20 400 0 L400 80 L0 80 Z" fill="#f3c31b"/>
      <path d="M0 46 C130 18 270 28 400 10 L400 80 L0 80 Z" fill="#ffffff"/>
      <path d="M0 52 C140 28 280 36 400 22 L400 80 L0 80 Z" fill="#1f7fc3"/>
    </symbol>
  </defs>
</svg>

<section class="sheet card-back">
  <div class="brand"><span class="brand-mark"></span><span class="brand-name">Voltmark Advisory<br>Group</span></div>
  <div class="company-details">
    Voltmark Advisory Group<br>
    C/o Miles R. Dunstan Esq.<br>
    Coral Court and West Ridge Road<br>
    P.O. Box K-57819<br>
    office - 242-555-0193<br>
    USA Cel # 832-555-0146<br>
    twellsby@voltmarkadvisorygroup.example
  </div>
  <div class="person">
    <div class="person-name">Tom Wellsby</div>
    <div class="person-title">Operations Manager</div>
  </div>
  <svg class="swoosh" height="60"><use href="#wave"/></svg>
</section>

<section class="sheet card-front">
  <div class="brand"><span class="brand-mark"></span><span class="brand-name">Voltmark Advisory<br>Group</span></div>
  <svg class="swoosh" height="90"><use href="#wave"/></svg>
</section>

<section class="sheet envelope-back">
  <svg class="flap" viewBox="0 0 439 233" preserveAspectRatio="none">
    <path d="M0 0 L219 150 L439 0" fill="none" stroke="#d9d9d9" stroke-width="1.2"/>
  </svg>
  <div class="brand"><span class="brand-mark"></span><span class="brand-name">Voltmark</span></div>
  <div class="web">www.voltmarkadvisorygroup.example</div>
  <svg class="swoosh" height="36"><use href="#wave"/></svg>
</section>

<section class="sheet envelope-front">
  <div class="brand"><span class="brand-mark"></span><span class="brand-name">Voltmark Advisory<br>Group</span></div>
  <div class="return-address">
    Voltmark Advisory Group<br>
    C/o Miles R. Dunstan Esq.<br>
    Coral Court and West Ridge Road<br>
    P.O. Box K-57819<br>
    Nassau, New Providence, The Bahamas
  </div>
  <svg class="swoosh" height="70"><use href="#wave"/></svg>
  <div class="web">www.voltmarkadvisorygroup.example</div>
</section>

<section class="sheet letterhead">
  <div class="brand"><span class="brand-mark"></span><span class="brand-name">Voltmark Advisory<br>Group</span></div>
  <div class="contact">
    Voltmark Advisory Group, C/o Miles R. Dunstan Esq.<br>
    Coral Court and West Ridge Road, P.O. Box K-57819<br>
    Nassau, New Providence, The Bahamas<br>
    P : office - 242-555-0193<br>
    C : 242-555-0178<br>
    E : twellsby@voltmarkadvisorygroup.example
  </div>
  <svg class="swoosh" height="80"><use href="#wave"/></svg>
  <div class="web">www.voltmarkadvisorygroup.example</div>
</section>

</body>
</html>
```